New business card for KT4 Linkway, a marketing company.

We need a new business card design. We would like it to be blue gray and white. We would like some movement but in a more subtle pattern than in the file we uploaded. We are a marketing company that connects brands with their target audiences - we make connections. We work in the New York Metro area with sophisticated clients. The card should feel modern, upscale and professional.

Target Market(s)

Businesses looking to grow their brands in tourism and nightlife. We work with liquor and beer companies and with Tourism bureaus and companies.

Industry/Entity Type

Marketing

Contact Information for Business Card

Would like a horizontal layout, two-sided. Would like the logo on the back with the tagline ' "connecting brands to their target audiences" under the logo. On the front, we would like name, title, contact email, contact phone, website.

Font styles to use
Sans Serif

Colors
3377b5
85cae6
ffffff

Requirements
Must have
• Our logo. See attached. Otherwise, open to your ideas.
Should not have
• No colors we don't want - no reds/pinks/oranges please

```html
<!DOCTYPE html>
<html lang="en">
<head>
<meta charset="utf-8">
<title>KT4 Linkway — Business Card</title>
<link rel="stylesheet" href="https://fonts.googleapis.com/css2?family=Questrial&display=swap">
<style>
  :root {
    --brand-blue: #3377b5;
    --sky-blue: #85cae6;
    --white: #ffffff;
    --backdrop: #e6e8eb;
    --card-shadow: rgba(20, 40, 70, 0.18);
  }
  * { box-sizing: border-box; margin: 0; padding: 0; }
  html, body {
    width: 1200px; height: 1200px; overflow: hidden;
    background: var(--backdrop);
    font-family: "Questrial", sans-serif;
  }
  .sheet {
    width: 1200px; height: 1200px;
    display: flex; flex-direction: column; align-items: center; justify-content: center;
    gap: 40px;
  }
  .card {
    position: relative;
    width: 900px; height: 514px;
    overflow: hidden;
    box-shadow: 0 10px 30px var(--card-shadow);
  }
  .card-art { position: absolute; inset: 0; width: 100%; height: 100%; }

  /* Front */
  .front-name {
    position: absolute; top: 78px; right: 60px;
    font-size: 40px; letter-spacing: 3px; color: var(--brand-blue);
  }
  .holder {
    position: absolute; left: 58px; top: 318px; color: var(--white);
  }
  .holder-name { font-size: 34px; letter-spacing: 0.5px; }
  .holder-title { font-size: 17px; letter-spacing: 1px; opacity: 0.85; margin-top: 4px; }
  .contact-list {
    position: absolute; left: 58px; top: 410px;
    list-style: none; color: var(--white); font-size: 18px;
  }
  .contact-list li { display: flex; align-items: center; gap: 12px; height: 28px; }
  .contact-icon { width: 22px; height: 22px; flex: none; }
  .address {
    position: absolute; right: 60px; top: 410px;
    color: var(--white); font-size: 17px; font-style: normal;
    text-align: right; line-height: 1.65;
  }

  /* Back */
  .card-back { background: var(--brand-blue); }
  .back-lockup {
    position: absolute; inset: 0;
    display: flex; flex-direction: column; align-items: center; justify-content: center;
    gap: 22px;
  }
  .back-name { font-size: 64px; color: var(--white); letter-spacing: 6px; }
  .back-rule { width: 120px; height: 3px; background: var(--sky-blue); }
  .tagline {
    font-size: 20px; letter-spacing: 3px; color: var(--white);
  }
</style>
</head>
<body>
<main class="sheet">

  <section class="card card-front" aria-label="Card front">
    <svg class="card-art" viewBox="0 0 900 514" preserveAspectRatio="none" aria-hidden="true">
      <rect width="900" height="514" fill="var(--brand-blue)"/>
      <polygon points="0,0 900,0 900,230 0,130" fill="var(--white)"/>
      <polygon points="0,142 900,242 900,250 0,150" fill="var(--sky-blue)"/>
      <polygon points="0,166 900,266 900,269 0,169" fill="var(--sky-blue)" opacity="0.6"/>
    </svg>

    <p class="front-name">KT4 LINKWAY</p>

    <div class="holder">
      <p class="holder-name">YOUR GOOD NAME</p>
      <p class="holder-title">TITLE</p>
    </div>

    <ul class="contact-list">
      <li>
        <svg class="contact-icon" viewBox="0 0 22 22" aria-hidden="true">
          <circle cx="11" cy="11" r="11" fill="var(--white)"/>
          <rect x="5" y="7" width="12" height="8" fill="none" stroke="var(--brand-blue)" stroke-width="1.5"/>
          <path d="M5 7 L11 12 L17 7" fill="none" stroke="var(--brand-blue)" stroke-width="1.5"/>
        </svg>
        hello@kt4linkway.com
      </li>
      <li>
        <svg class="contact-icon" viewBox="0 0 22 22" aria-hidden="true">
          <circle cx="11" cy="11" r="11" fill="var(--white)"/>
          <path d="M7 6 C6 10 10 15 15 16 L16 14 L13.5 12.5 L12.5 13.5 C11 13 9 11 8.5 9.5 L9.5 8.5 L8 6 Z" fill="var(--brand-blue)"/>
        </svg>
        555-308-2716
      </li>
      <li>
        <svg class="contact-icon" viewBox="0 0 22 22" aria-hidden="true">
          <circle cx="11" cy="11" r="11" fill="var(--white)"/>
          <circle cx="11" cy="11" r="6" fill="none" stroke="var(--brand-blue)" stroke-width="1.4"/>
          <ellipse cx="11" cy="11" rx="2.6" ry="6" fill="none" stroke="var(--brand-blue)" stroke-width="1.2"/>
          <path d="M5 11 H17" stroke="var(--brand-blue)" stroke-width="1.2"/>
        </svg>
        kt4linkway.com
      </li>
    </ul>

    <address class="address">128 Harbor Lane,<br>New York NY</address>
  </section>

  <section class="card card-back" aria-label="Card back">
    <div class="back-lockup">
      <p class="back-name">KT4 LINKWAY</p>
      <span class="back-rule"></span>
      <p class="tagline">BRINGING BRANDS AND AUDIENCES TOGETHER</p>
    </div>
  </section>

</main>
</body>
</html>
```